Newsletter for a recent surgical mission conducted by Bright Path Outreach

We need a one page, two sided newsletter reporting the events of our recent mission trip. The first page should have the title Bright Path Outreach along with the mission date of November 2019 and Cayo, Belize as the location. We want to highlight the pictures of the children especially the before and after pictures. Pictures of the hospital and ward should give the viewer the feel that they visited the hospital with us and to show how basic and rustic it is. Maybe stock photos of mountainous green landscape would help.

Target Market(s)

Our donors receive this and we want to highlight what we did and how their contributions enabled us to do it.

Industry/Entity Type

Non Profit

Font styles to use
Sans Serif

Colors

Designer to choose colors to be used in the design.

Requirements
Must have
• 1. The organization logo
• 2. Please match the text describing each patient to the corresponding pictures of the patients.
• 3. Highlighted text thanking our donors for donating.
• 4. www.brightpathoutreach should be included which is our website.
• 5. Text asking anyone who wants to contribute to our next mission to visit the Donate link on our website.
Nice to have
• 1. Stock images of the Belizean landscape can be used along with the picture of the hospital.
• 2. I am not sure what 'GREYSCALE" is but it might be interesting to see what a version of the newsletter looks like in that color. We have always matched the colors in the logo. If not, then just match the colors in the logo but let the designer choose.
Should not have
• When including the picture of us the surgeons, keep it small. We want to highlight the patients NOT the staff.

```html
<!DOCTYPE html>
<html lang="en">
<head>
<meta charset="utf-8">
<title>Bright Path Outreach – Mission Newsletter, Page 2</title>
<link href="https://fonts.googleapis.com/css2?family=Bitter:ital,wght@0,400;1,400&family=Source+Sans+3:wght@400;600&display=swap" rel="stylesheet">
<style>
  :root{
    --backdrop:#e6e7e8;
    --paper:#ffffff;
    --paper-tint:#f3f4f5;
    --ink:#1f2326;
    --rule:#8c9399;
    --band:#5d7282;
    --band-ink:#ffffff;
    --photo-warm:#c9b8a6;
    --photo-ward:#8fb7a0;
    --photo-blue:#6f8fb8;
    --photo-child:#d9cbc0;
  }
  *{box-sizing:border-box;margin:0;padding:0}
  html,body{width:1200px;height:1036px;overflow:hidden;background:var(--backdrop)}
  .sheet{position:absolute;left:200px;top:0;width:800px;height:1036px;background:var(--paper);
    display:flex;flex-direction:column;box-shadow:0 4px 18px rgba(0,0,0,.18)}
  .story{position:relative;display:flex;height:234px}
  .story + .story::before{content:"";position:absolute;left:0;right:0;top:-8px;height:16px;
    background:none}
  .curve{position:absolute;left:0;top:-10px;width:800px;height:20px;pointer-events:none}
  .photos{display:flex;height:100%;gap:4px}
  .photo{height:100%}
  .caption{flex:1;display:flex;align-items:center;padding:0 34px;
    font-family:"Bitter",Georgia,serif;font-size:14.5px;line-height:1.38;color:var(--ink);background:var(--paper-tint)}
  .caption.italic{font-style:italic}
  .footer{margin-top:auto;height:100px;background:var(--band);color:var(--band-ink);
    font-family:"Source Sans 3",Arial,sans-serif;display:flex;flex-direction:column;justify-content:center;padding-left:170px}
  .footer .org{font-size:15px;font-weight:600;letter-spacing:.02em}
  .footer .contact{font-size:15px;margin-top:2px}
  .story.last{height:234px}
</style>
</head>
<body>
<main class="sheet">

  <section class="story">
    <div class="photos" style="width:430px">
      <div class="photo" style="width:170px;background:linear-gradient(160deg,#e9eef0,var(--photo-warm))" role="img" aria-label="Patient's healed forearm resting on a hospital bed"></div>
      <div class="photo" style="width:256px;background:linear-gradient(160deg,#d8dde0,var(--photo-blue))" role="img" aria-label="Surgeon in blue scrubs seated beside the adult patient"></div>
    </div>
    <p class="caption italic">This is Marco Velez, a 23 year old man from the town of Santa Elena in Cayo. He sustained a left upper arm injury from a rotating saw four years ago that lacerated his radial nerve. It was never repaired and now he cannot extend his wrist, thumb and fingers. The Team performed forearm muscle and tendon transfers which after a 6-week recovery will allow him to get back to work doing construction.</p>
  </section>

  <section class="story">
    <svg class="curve" viewBox="0 0 800 20" aria-hidden="true"><path d="M40 16 Q400 2 760 16" fill="none" stroke="var(--rule)" stroke-width="1"/></svg>
    <p class="caption">This is Lina Morales from the small town of Spanish Lookout in Cayo, Belize. Lina is 5 months old and was born with a cleft lip and palate. The Team was able to help her by performing the 1st of 4 surgeries she will need to reconstruct her lip, palate and nose.</p>
    <div class="photos" style="width:470px">
      <div class="photo" style="width:170px;background:linear-gradient(160deg,#eef0f2,var(--photo-child))" role="img" aria-label="Infant patient before cleft lip surgery"></div>
      <div class="photo" style="width:170px;background:linear-gradient(160deg,#f0ecea,var(--photo-child))" role="img" aria-label="Infant patient after cleft lip repair"></div>
      <div class="photo" style="width:122px;background:linear-gradient(160deg,#9fcf8a,#b84a4a)" role="img" aria-label="Father holding the infant in the ward"></div>
    </div>
  </section>

  <section class="story">
    <svg class="curve" viewBox="0 0 800 20" aria-hidden="true"><path d="M40 16 Q400 2 760 16" fill="none" stroke="var(--rule)" stroke-width="1"/></svg>
    <div class="photos" style="width:460px">
      <div class="photo" style="width:150px;background:linear-gradient(160deg,#e3e6ea,var(--photo-blue))" role="img" aria-label="Small group photo of the surgical team"></div>
      <div class="photo" style="width:306px;background:linear-gradient(160deg,#7fc96a,var(--photo-ward) 55%,#d8b04a)" role="img" aria-label="Brightly painted pediatric ward with families waiting"></div>
    </div>
    <p class="caption">The Valley Regional Medical Center in Belmopan is the secondary receiving center for all of the smaller community hospitals and clinics throughout all of the Cayo District. It maintains a large clinic system, Emergency Room, two operating rooms, and an adult, maternity, and pediatric ward totaling 40 beds. The BPO Team was fortunate to partner with the doctors and staff there doing our work.</p>
  </section>

  <section class="story last">
    <svg class="curve" viewBox="0 0 800 20" aria-hidden="true"><path d="M40 16 Q400 2 760 16" fill="none" stroke="var(--rule)" stroke-width="1"/></svg>
    <p class="caption">This is 5 year old Teo Ramirez with his Mom and Dad. They are from the Frank's Eddy Village in Belize. Teo had his cleft lip and palate repaired when he was younger. Unfortunately, he developed an opening in the roof of his mouth afterwards (palatal fistula) that results in liquid and food in his mouth coming out his nose when he ate. The Team was able to repair his palate this week and in a short time get back to eating normally.</p>
    <div class="photos" style="width:440px">
      <div class="photo" style="width:200px;background:linear-gradient(160deg,#cfe3ee,var(--photo-child))" role="img" aria-label="Young boy in a surgical cap before his palate repair"></div>
      <div class="photo" style="width:236px;background:linear-gradient(160deg,#eeeeee,#d9736f 60%,#3f4f6a)" role="img" aria-label="The boy standing with his mother and father"></div>
    </div>
  </section>

  <footer class="footer">
    <p class="org">THE BRIGHT PATH OUTREACH FOUNDATION, 418 Harbor Lane, Riverton, New York</p>
    <p class="contact">Website: www.brightpathoutreach.com | Email: staff@brightpathoutreach.com</p>
  </footer>

</main>
</body>
</html>
```